Professional and creatice Life Coach - Business Card design

I just relaunched my website and now i a need a correspoonding business card for my task as life coach. My website is www.tbalrond.com as reference. The compass is kind of a symbol for my work, as I help people navigate through their challenging phases in life. The business card should be colorful, but not too playful as I also adress business people. So it sould be creative, but professional (also to suport my other business as Management Consultant)

Target Market(s)

People who want to get teir problems resolved, in business, partnership and other personal realms

Industry/Entity Type

Life Coaching

Contact Information for Business Card

Front side should include Name, Phone number, Email, Website and address

Font styles to use
Sans Serif

Colors
add136

Requirements
Must have
• "Mag. Leopold Brantner" -> Name
"Energetische Praxis" -> Jobtitle (describing my profession as life coach)
colours and style should match my website www.tbalrond.com
Nice to have
• a compass as a symbol

```html
<!DOCTYPE html>
<html lang="de">
<head>
<meta charset="utf-8">
<title>Leopold Brantner – Visitenkarte</title>
<link href="https://fonts.googleapis.com/css2?family=Montserrat:wght@300;500&family=Playfair+Display:wght@400&display=swap" rel="stylesheet">
<style>
  :root {
    --lime: #add136;
    --card: #0c0c0c;
    --stage: #2a2c30;
    --text-light: #d6d6d6;
    --white: #ffffff;
  }
  * { margin: 0; padding: 0; box-sizing: border-box; }
  html, body { width: 1200px; height: 900px; overflow: hidden; }
  body {
    background: var(--stage);
    font-family: "Montserrat", sans-serif;
    position: relative;
  }
  .card {
    position: absolute;
    left: 320px;
    width: 560px;
    height: 320px;
    background: var(--card);
    border: 3px solid var(--lime);
    overflow: hidden;
  }
  .card--front { top: 100px; }
  .card--back { top: 480px; }

  .brand {
    position: absolute;
    display: flex;
    align-items: center;
    gap: 12px;
    color: var(--lime);
    font-family: "Playfair Display", serif;
    font-weight: 400;
    white-space: nowrap;
  }
  .brand__dot {
    border-radius: 50%;
    background: var(--lime);
    flex: none;
  }
  .card--front .brand { left: 34px; top: 30px; font-size: 26px; }
  .card--front .brand__dot { width: 22px; height: 22px; }
  .card--back .brand { left: 70px; top: 126px; font-size: 40px; }
  .card--back .brand__dot { width: 32px; height: 32px; }

  .holder {
    position: absolute;
    left: 34px;
    top: 150px;
    padding-left: 10px;
    border-left: 2px solid var(--lime);
  }
  .holder__name {
    color: var(--lime);
    font-weight: 500;
    font-size: 17px;
    line-height: 1.2;
  }
  .holder__title {
    color: var(--text-light);
    font-weight: 300;
    font-size: 10px;
    margin-top: 2px;
  }

  .contacts {
    position: absolute;
    right: 100px;
    top: 130px;
    list-style: none;
    text-align: right;
  }
  .contacts li {
    color: var(--text-light);
    font-weight: 300;
    font-size: 16px;
    height: 38px;
    line-height: 38px;
  }

  .contact-band {
    position: absolute;
    right: 44px;
    top: 0;
    width: 40px;
    height: 292px;
    background: var(--lime);
    border-radius: 0 0 20px 20px;
  }
  .contact-band__icon {
    position: absolute;
    left: 9px;
    width: 22px;
    height: 22px;
  }
</style>
</head>
<body>

  <section class="card card--front" aria-label="Vorderseite">
    <div class="brand"><span class="brand__dot"></span>Leopold Brantner</div>

    <div class="holder">
      <p class="holder__name">Mag. Leopold Brantner</p>
      <p class="holder__title">Energetische Praxis</p>
    </div>

    <ul class="contacts">
      <li>012 987 65430</li>
      <li>leo@brantnermail.com</li>
      <li>www.tbalrond.com</li>
      <li>B14-block /D street K07-Uk</li>
    </ul>

    <div class="contact-band">
      <svg class="contact-band__icon" style="top:138px" viewBox="0 0 24 24" fill="none" stroke="#fff" stroke-width="1.6" stroke-linecap="round" stroke-linejoin="round" aria-label="Telefon">
        <path d="M6 3h3l1.5 4-2 1.5a11 11 0 0 0 7 7l1.5-2 4 1.5v3a2 2 0 0 1-2 2A17 17 0 0 1 4 5a2 2 0 0 1 2-2z"/>
      </svg>
      <svg class="contact-band__icon" style="top:176px" viewBox="0 0 24 24" fill="none" stroke="#fff" stroke-width="1.6" stroke-linejoin="round" aria-label="E-Mail">
        <rect x="3" y="6" width="18" height="12"/>
        <path d="M3 6l9 7 9-7M3 18l7-6M21 18l-7-6"/>
      </svg>
      <svg class="contact-band__icon" style="top:214px" viewBox="0 0 24 24" fill="none" stroke="#fff" stroke-width="1.6" aria-label="Webseite">
        <circle cx="12" cy="12" r="9"/>
        <ellipse cx="12" cy="12" rx="4" ry="9"/>
        <path d="M3 12h18M5 7.5h14M5 16.5h14"/>
      </svg>
      <svg class="contact-band__icon" style="top:252px" viewBox="0 0 24 24" fill="none" stroke="#fff" stroke-width="1.6" stroke-linejoin="round" aria-label="Adresse">
        <path d="M12 21s-6-6.2-6-11a6 6 0 0 1 12 0c0 4.8-6 11-6 11z"/>
        <circle cx="12" cy="10" r="2.2"/>
      </svg>
    </div>
  </section>

  <section class="card card--back" aria-label="Rückseite">
    <div class="brand"><span class="brand__dot"></span>Leopold Brantner</div>
  </section>

</body>
</html>
```